Women's Shelter Website Design

We are working with a Women's Shelter in California. They provide services and shelter for women and mothers throughout California.
Some sites to use for inspiration:
https://harborlightcommons.org
https://qbrtl.org
https://www.kemjy.org
https://plmfarrowby.org
https://www.gvhollow.org (I love the banner, navigation and upper navigation)
https://bellmereroost.org (love the idea of an EXIT NOW button)
Thank you for taking the time to consider designing a website for us. We are web developers based in Stockton, CA, USA. Most of our projects go through the same process. Understanding this process may help you win a project with us. We custom-code all of our websites in-house. We don’t have any requirements as to what tools you use for your design, but we ask that you follow these guidelines.
IMAGES:
If you use any images or icons in the design, we ask that you have a link to the asset so we can purchase the image/icon. Most of the designs we submit do not have the customer’s images on them unless they have some great images. Be creative; show us the feeling you are trying to portray with your image choices. Use any royalty-free site you choose. We subscribe to Adobe and mainly use their images, but we can purchase images outside of Adobe. PLEASE NOTE: we will not submit designs to clients with watermarks on the images.
FONTS:
We ask that you identify the fonts you’re using in the design. This can be done in a message if you want. We typically use Google Fonts and Adobe Fonts.
CONTENT:
We're always open to different content and ideas. We often submit designs with stock images so the client can see our vision. We typically take pictures after the website launch to use their images with our vision. Lorem Ipsum is fine for paragraphs, but we ask that you make the Headers with correct English. We want to be able to show the vision and identify the sections of the website.
INSPIRATION:
We typically add a couple of links in the brief of websites we like to help you get started in your design.
REVISIONS:
We do not often ask for revisions of the designs unless we see something in the design that may not appeal to the client. If there are slight changes that we want to make, we do that in the development process.
FEEDBACK:
We rarely give feedback on designs during the design process. We are working on many website projects and do not have the time to provide feedback. We usually respond if your request is well thought out and asks specific questions, but a note asking “feedback, please” usually goes unanswered.

```html
<!DOCTYPE html>
<html lang="en">
<head>
<meta charset="utf-8">
<title>Amberlea Womens Shelter</title>
<link href="https://fonts.googleapis.com/css2?family=Montserrat:wght@500;600;700;800&family=Poppins:wght@400;500;600&display=swap" rel="stylesheet">
<style>
:root{
  --purple:#5f3596;
  --purple-deep:#4a2478;
  --coral:#f47b5c;
  --coral-pale:#fde3db;
  --green:#4fbf5a;
  --ink:#1d1d1f;
  --text:#4a4a4a;
  --dark:#323232;
  --card:#444444;
  --footer:#1f1f1f;
  --white:#ffffff;
}
*{box-sizing:border-box;margin:0;padding:0}
html,body{width:1200px;height:5107px;overflow:hidden}
body{font-family:"Poppins",sans-serif;color:var(--text);background:var(--white);position:relative}
h1,h2,h3,h4,.logo-name{font-family:"Montserrat",sans-serif;color:var(--ink)}
section,header,footer,.topbar{position:absolute;left:0;width:1200px}
.abs{position:absolute}
p{font-size:12px;line-height:24px}

/* top bar */
.topbar{top:0;height:58px;display:flex}
.topbar a{flex:1;display:flex;align-items:center;justify-content:center;gap:22px;color:#fff;font:700 12px "Montserrat",sans-serif;text-decoration:none;text-transform:uppercase}
.topbar a::before,.topbar a::after{content:"";width:56px;height:1px;background:rgba(255,255,255,.8)}
.tb-help{background:var(--purple)}.tb-vol{background:var(--coral)}.tb-don{background:var(--green)}

/* header */
.site-header{top:58px;height:154px;background:#fff}
.logo{left:124px;top:52px;display:flex;align-items:center;gap:10px}
.logo-mark{width:26px;height:26px;border-radius:50%;background:var(--purple)}
.logo-name{font-weight:800;font-size:26px;color:var(--ink)}
.main-nav{left:300px;top:24px;width:780px;display:flex;justify-content:space-between;font-size:11px;color:#333}
.signup{left:302px;top:62px;width:773px;height:72px;background:linear-gradient(90deg,var(--purple),var(--coral));display:flex;align-items:center;gap:8px;padding:0 15px}
.signup span{height:40px;background:#fff;flex:1;font-size:11px;padding:12px 18px;color:#333}
.signup b{width:172px;height:40px;border:2px solid #fff;background:var(--coral);color:#fff;font:600 11px "Poppins",sans-serif;display:flex;align-items:center;justify-content:center}

/* hero */
.hero{top:212px;height:668px;background:linear-gradient(100deg,#5b2f98 0%,#6d44a3 45%,#7f6799 70%,#8d8497 100%)}
.hero h1{left:124px;top:135px;font-size:52px;line-height:63px;font-weight:800;color:#fff;width:760px;white-space:nowrap}
.hero p{left:124px;top:345px;width:460px;color:#fff;font-size:12px}
.btn{display:flex;align-items:center;justify-content:center;color:#fff;font:600 11px "Poppins",sans-serif}
.hero .btn{left:124px;top:454px;width:240px;height:40px;background:var(--coral)}
.scroll-line{left:133px;top:522px;width:2px;height:62px;background:#fff}
.mouse{left:126px;top:608px;width:14px;height:24px;border:2px solid #fff;border-radius:8px}
.dots{left:898px;top:593px;display:flex;gap:14px}
.dots i{width:24px;height:24px;border-radius:50%;background:rgba(40,30,60,.55);color:#fff;font:500 8px "Poppins",sans-serif;font-style:normal;display:flex;align-items:center;justify-content:center}
.dots i.on{background:var(--green)}

/* about */
.about{top:880px;height:855px}
.about .frame{left:108px;top:100px;width:160px;height:580px;background:var(--coral)}
.about .photo{left:124px;top:115px;width:466px;height:605px;background:linear-gradient(160deg,#d9d9d9,#8e8e8e 60%,#6a6a6a)}
.about .accent{left:145px;top:680px;width:15px;height:70px;background:var(--green)}
.about h2{left:637px;top:173px;font-size:44px;line-height:52px;font-weight:800}
.about h2 em,.impact h2 em,.values h2 em,.news h2 em{font-style:normal;color:var(--purple)}
.about .copy{left:637px;top:302px;width:440px;font-size:12.5px}
.about h3{left:637px;top:420px;font-size:28px;font-weight:700;color:var(--coral)}
.about .copy2{left:637px;top:478px;width:440px;font-size:12.5px}
.about .btn{left:637px;top:617px;width:240px;height:40px;background:var(--green)}

/* impact */
.impact{top:1735px;height:735px;background:var(--dark)}
.impact .stripe-g{left:1135px;top:0;width:18px;height:735px;background:var(--green)}
.impact .stripe-p{left:1165px;top:0;width:18px;height:735px;background:var(--purple)}
.impact h2{left:0;width:1200px;top:92px;text-align:center;font-size:44px;line-height:52px;font-weight:800;color:#fff}
.impact h2 em{color:var(--coral)}
.impact .lead{left:290px;top:222px;width:620px;text-align:center;color:#e6e6e6}
.stat{top:335px;width:303px;height:300px;background:var(--card);text-align:center;padding:52px 40px 0}
.stat h4{color:#fff;font-size:24px;line-height:30px;font-weight:800}
.stat p{color:#e3e3e3;margin-top:20px;font-size:11px;line-height:22px}

/* values */
.values{top:2470px;height:538px}
.values h2{left:124px;top:88px;font-size:44px;font-weight:800}
.values .lead{left:124px;top:166px;width:760px}
.value{top:262px;width:140px;text-align:center}
.value .ring{width:132px;height:132px;margin:0 auto;border-radius:50%;background:var(--coral-pale);display:flex;align-items:center;justify-content:center}
.value .core{width:92px;height:92px;border-radius:50%;background:var(--coral);display:flex;align-items:center;justify-content:center}
.value h4{margin-top:30px;font-size:15px;font-weight:700}

/* space for change */
.change{top:3008px;height:640px;background:linear-gradient(180deg,#6a3fa6 0%,#5b2f98 60%,#51288c 100%)}
.change h2{left:0;width:1200px;top:118px;text-align:center;color:#fff;font-size:44px;font-weight:800}
.change h2 em{font-style:normal;color:var(--coral)}
.change .sub{left:0;width:1200px;top:192px;text-align:center;color:#fff;font-size:16px}
.change .p1{left:225px;top:250px;width:750px;text-align:center;color:#f1ecf8}
.change .p2{left:225px;top:410px;width:750px;text-align:center;color:#f1ecf8}
.change .rule{left:520px;top:502px;width:162px;height:3px;background:var(--green)}

/* news */
.news{top:3648px;height:847px}
.news h2{left:124px;top:68px;font-size:44px;line-height:52px;font-weight:800}
.news .lead{left:124px;top:216px;width:760px}
.post{top:320px;width:303px}
.post .pic{height:187px}
.post .date{margin-top:58px;font-size:10px;color:var(--coral)}
.post h4{font-size:18px;font-weight:700;margin-top:2px}
.post p{font-size:11px;line-height:22px;margin-top:12px}
.post .more{margin-top:42px;font:600 11px "Poppins",sans-serif;color:var(--purple);display:flex;align-items:center;gap:14px}
.post .more::after{content:"";width:50px;height:1px;background:var(--purple)}

/* footer */
.site-footer{top:4495px;height:545px;background:var(--footer)}
.site-footer .logo{left:0;width:1200px;justify-content:center;top:105px}
.site-footer .logo-name{color:#fff;font-size:34px}
.site-footer .blurb{left:340px;top:220px;width:520px;text-align:center;color:#ddd;font-size:11px;line-height:22px}
.site-footer .rule{left:124px;width:870px;height:1px;background:var(--coral)}
.foot-nav{left:124px;top:350px;width:870px;display:flex;justify-content:center;gap:35px;font-size:11px;color:#eee}
.social{left:0;width:1200px;top:424px;display:flex;justify-content:center;gap:20px}
.social i{width:44px;height:44px;border-radius:50%;border:2px solid #fff}
.copyright{top:5040px;height:67px;background:#f2f2f2;display:flex;align-items:center;justify-content:center;font-size:12px;color:#444}
</style>
</head>
<body>

<nav class="topbar">
  <a class="tb-help" href="#">Get Help Now</a>
  <a class="tb-vol" href="#">Volunteer</a>
  <a class="tb-don" href="#">Dontate</a>
</nav>

<header class="site-header">
  <div class="logo abs"><span class="logo-mark"></span><span class="logo-name">Amberlea</span></div>
  <div class="main-nav abs">
    <span>Open Door Campaign</span><span>Who We Are</span><span>What We Do</span><span>Real Stories</span><span>Ways To Give</span><span>Get Involved</span><span>Contact Us</span>
  </div>
  <div class="signup abs"><span>Name</span><span>Email</span><b>Sign Up Now!</b></div>
</header>

<section class="hero" role="img" aria-label="Photo of a thoughtful woman under a purple overlay">
  <h1 class="abs">A Women Shelter<br>That Offers More Than<br>Just A Roof</h1>
  <p class="abs">Lorem Ipsum Is Simply Dummy Text Of The Printing And Typesetting Industry. Lorem Ipsum Has Been The Industry's Standard Dummy Text Ever Since The 1500s,</p>
  <a class="btn abs">Give Help That Works</a>
  <span class="scroll-line abs"></span>
  <span class="mouse abs"></span>
  <div class="dots abs"><i class="on">01</i><i>02</i><i>03</i><i>04</i><i>05</i></div>
</section>

<section class="about">
  <div class="frame abs"></div>
  <div class="photo abs" role="img" aria-label="Photo of smiling volunteers in a huddle, seen from below"></div>
  <div class="accent abs"></div>
  <h2 class="abs">About The<br>Women <em>Shelter</em></h2>
  <p class="copy abs">Lorem Ipsum Is Simply Dummy Text Of The Printing And Typesetting Industry. Lorem Ipsum Has Been The Industry's Standard Dummy Text Ever Since The 1500s, When An Unknown Printer Took A Galley Of Type.</p>
  <h3 class="abs">Our Mission</h3>
  <p class="copy2 abs">Lorem Ipsum Is Simply Dummy Text Of The Printing And Typesetting Industry. Lorem Ipsum Has Been The Industry's Standard Dummy Text Ever Since The 1500s, When An Unknown Printer Took A Galley Of Type.</p>
  <a class="btn abs">About The Women Shelter</a>
</section>

<section class="impact">
  <div class="stripe-g abs"></div><div class="stripe-p abs"></div>
  <h2 class="abs">Our Impact At A<br><em>Glance</em></h2>
  <p class="lead abs">Lorem Ipsum Is Simply Dummy Text Of The Printing And Typesetting Industry. Lorem Ipsum Has Been The Industry's Standard Dummy Text Ever Since The 1500s, When An Unknown Printer Took A Galley Of Type.</p>
  <div class="stat abs" style="left:124px"><h4>500<br>Individuals</h4><p>Lorem Ipsum Is Simply Dummy Text Of The Printing And Typesetting Industry. Lorem Ipsum Has Been The Industry's Standard Dummy Text Ever Since The 1500s,</p></div>
  <div class="stat abs" style="left:448px"><h4>6,500<br>Safe Nights</h4><p>Lorem Ipsum Is Simply Dummy Text Of The Printing And Typesetting Industry. Lorem Ipsum Has Been The Industry's Standard Dummy Text Ever Since The 1500s,</p></div>
  <div class="stat abs" style="left:772px"><h4>275<br>Hours</h4><p>Lorem Ipsum Is Simply Dummy Text Of The Printing And Typesetting Industry. Lorem Ipsum Has Been The Industry's Standard Dummy Text Ever Since The 1500s,</p></div>
</section>

<section class="values">
  <h2 class="abs">Our <em>Values</em></h2>
  <p class="lead abs">Lorem Ipsum Is Simply Dummy Text Of The Printing And Typesetting Industry. Lorem Ipsum Has Been The Industry's Standard Dummy Text Ever Since The 1500s, When An Unknown Printer Took A Galley Of Type.</p>
  <div class="value abs" style="left:120px"><div class="ring"><div class="core">
    <svg width="40" height="40" viewBox="0 0 40 40" fill="none" stroke="#fff" stroke-width="2.5"><path d="M20 4 L33 9 V19 C33 28 27 33 20 36 C13 33 7 28 7 19 V9 Z"/><path d="M14 20 L18 24 L26 15"/></svg>
  </div></div><h4>Safety</h4></div>
  <div class="value abs" style="left:307px"><div class="ring"><div class="core">
    <svg width="40" height="40" viewBox="0 0 40 40" fill="#fff"><path d="M20 34 L6 20 C1 15 4 6 11 6 C15 6 18 9 20 12 C22 9 25 6 29 6 C36 6 39 15 34 20 Z"/></svg>
  </div></div><h4>Respect</h4></div>
  <div class="value abs" style="left:495px"><div class="ring"><div class="core">
    <svg width="40" height="40" viewBox="0 0 40 40" fill="none" stroke="#fff" stroke-width="2.5"><path d="M20 8 V32"/><path d="M20 16 C14 10 8 12 8 18 C8 24 14 28 20 32 C26 28 32 24 32 18 C32 12 26 10 20 16"/></svg>
  </div></div><h4>Stewardship</h4></div>
  <div class="value abs" style="left:682px"><div class="ring"><div class="core">
    <svg width="40" height="40" viewBox="0 0 40 40" fill="none" stroke="#fff" stroke-width="2.5"><path d="M20 6 V34 M12 34 H28 M8 11 H32"/><path d="M8 11 L4 22 H12 Z M32 11 L28 22 H36 Z"/></svg>
  </div></div><h4>Social Justice</h4></div>
  <div class="value abs" style="left:870px"><div class="ring"><div class="core">
    <svg width="40" height="40" viewBox="0 0 40 40" fill="#fff"><circle cx="20" cy="13" r="5"/><circle cx="9" cy="16" r="4"/><circle cx="31" cy="16" r="4"/><path d="M11 32 C11 24 15 21 20 21 C25 21 29 24 29 32 Z"/><path d="M2 30 C2 24 5 22 9 22 C10 22 11 22 12 23 C10 25 9 28 9 30 Z M38 30 C38 24 35 22 31 22 C30 22 29 22 28 23 C30 25 31 28 31 30 Z"/></svg>
  </div></div><h4>Community</h4></div>
</section>

<section class="change" role="img" aria-label="Photo of two women sharing a moment on a sofa under a purple overlay">
  <h2 class="abs">Space For <em>Change</em></h2>
  <p class="sub abs">Lorem Ipsum Is Simply Dummy Text Of The Printing And Typesetting Industry.</p>
  <p class="p1 abs">Lorem Ipsum Is Simply Dummy Text Of The Printing And Typesetting Industry. Lorem Ipsum Has Been The Industry's Standard Dummy Text Ever Since The 1500s, When An Unknown Printer Took A Galley Of Type And Scrambled It To Make A Type Specimen Book. It Has Survived Not Only Five Centuries, But Also The Leap Into Electronic Typesetting, Remaining Essentially Unchanged. It Was Popularised In The 1960s With The Release Of Glyphset Sheets Containing Lorem Ipsum Passages, And More Recently With Desktop Publishing Software Like Typecraft Studio Including Versions Of Lorem Ipsum.</p>
  <p class="p2 abs">Lorem Ipsum Is Simply Dummy Text Of The Printing And Typesetting Industry. Lorem Ipsum Has Been The Industry's Standard Dummy Text Ever Since The 1500s, When An Unknown Printer Took A Galley Of Type And Scrambled It To Make A Type Specimen Book. It Has Survived Not Only Five Centuries,</p>
  <span class="rule abs"></span>
</section>

<section class="news">
  <h2 class="abs">Latest News &amp;<br><em>Blogs</em></h2>
  <p class="lead abs">Lorem Ipsum Is Simply Dummy Text Of The Printing And Typesetting Industry. Lorem Ipsum Has Been The Industry's Standard Dummy Text Ever Since The 1500s.</p>
  <article class="post abs" style="left:124px">
    <div class="pic" role="img" aria-label="Portrait photo of a young woman" style="background:linear-gradient(135deg,#3a2a24,#7a5444 60%,#2a1d19)"></div>
    <div class="date">01 August, 2023</div><h4>Where Can I Get Some?</h4>
    <p>Lorem Ipsum Is Simply Dummy Text Of The Printing And Typesetting Industry. Lorem Ipsum Has Been The Industry's Standard Dummy Text Ever Since The 1500s.</p>
    <a class="more">Read more</a>
  </article>
  <article class="post abs" style="left:448px">
    <div class="pic" role="img" aria-label="Photo of an older woman resting in a bright room" style="background:linear-gradient(135deg,#b9a79a,#d8cfc9 55%,#8c7a6f)"></div>
    <div class="date">01 August, 2023</div><h4>Where Can I Get Some?</h4>
    <p>Lorem Ipsum Is Simply Dummy Text Of The Printing And Typesetting Industry. Lorem Ipsum Has Been The Industry's Standard Dummy Text Ever Since The 1500s.</p>
    <a class="more">Read more</a>
  </article>
  <article class="post abs" style="left:772px">
    <div class="pic" role="img" aria-label="Photo of a smiling woman worker in safety gear" style="background:linear-gradient(135deg,#3d6f9a,#b9c86a 50%,#d9653a)"></div>
    <div class="date">01 August, 2023</div><h4>Where Can I Get Some?</h4>
    <p>Lorem Ipsum Is Simply Dummy Text Of The Printing And Typesetting Industry. Lorem Ipsum Has Been The Industry's Standard Dummy Text Ever Since The 1500s.</p>
    <a class="more">Read more</a>
  </article>
</section>

<footer class="site-footer">
  <div class="logo abs"><span class="logo-mark"></span><span class="logo-name">Amberlea</span></div>
  <p class="blurb abs">Lorem Ipsum Is Simply Dummy Text Of The Printing And Typesetting Industry. Lorem Ipsum Has Been The Industry's Standard Dummy Text Ever Since The 1500s.</p>
  <span class="rule abs" style="top:328px"></span>
  <div class="foot-nav abs"><span>Open Door Campaign</span><span>Who We Are</span><span>What We Do</span><span>Real Stories</span><span>Ways To Give</span><span>Get Involved</span><span>Contact Us</span></div>
  <span class="rule abs" style="top:386px"></span>
  <div class="social abs"><i aria-label="Social link one"></i><i aria-label="Social link two"></i><i aria-label="Social link three"></i></div>
</footer>
<div class="copyright abs" style="left:0;width:1200px">Copyright © 2023 Amberlea Womens Shelter</div>

</body>
</html>
```